Bref créative
Business Cards & Stationary For Law Firm - Use Existing Logo
Harlow Law Offices
I need double sided standard sized Business Card [3.5" x 2"]
I am open to different fonts for the info. I have used Century Gothic before but try any
Professional
Dorian P. Harlow, Esq.
482 N.E. 3rd Avenue
Suite 2206
Miami, Florida 33130
dph@harlowlo.example
www.harlowlo.example
To me the most important thing on a card is that they get your information quickly and easily. I see so many cards that are unmemorable and cluttered with tiny type. I think people want your name and phone easy to read and accessible.
Can put logo and/or any information on either side. Try different designs.

```html
<!DOCTYPE html>
<html lang="en">
<head>
<meta charset="utf-8">
<title>Harlow Law Offices – Business Card</title>
<link rel="stylesheet" href="https://fonts.googleapis.com/css2?family=Cinzel:wght@400;600&family=Lato:wght@400;700&display=swap">
<style>
  :root {
    --bg-light: #f1f2f4;
    --bg-dark: #d4d6da;
    --blue-light: #2a6ee0;
    --blue: #1b56c6;
    --blue-deep: #0c3a9c;
    --ink: #111418;
    --paper: #ffffff;
    --text: #2b3a5c;
  }
  * { box-sizing: border-box; margin: 0; padding: 0; }
  html, body { width: 1200px; height: 984px; overflow: hidden; }
  body {
    background: radial-gradient(ellipse at 50% 40%, var(--bg-light) 0%, var(--bg-dark) 100%);
    position: relative;
    font-family: "Lato", sans-serif;
  }
  .card {
    position: absolute;
    left: 250px;
    width: 700px;
    height: 400px;
    border-radius: 26px;
    overflow: hidden;
    box-shadow: 0 14px 30px rgba(0,0,0,0.18);
  }
  .card-front { top: 60px; background: radial-gradient(ellipse at 45% 40%, var(--blue-light) 0%, var(--blue) 55%, var(--blue-deep) 100%); }
  .card-back { top: 524px; background: var(--paper); }

  .front-brand {
    position: absolute; left: 0; right: 0; top: 150px;
    display: flex; align-items: center; justify-content: center; gap: 16px;
  }
  .front-brand .mark { width: 44px; height: 44px; background: var(--paper); }
  .front-brand .brand-name {
    font-family: "Cinzel", serif; font-weight: 400; font-size: 34px;
    color: var(--paper); letter-spacing: 2px;
  }
  .front-web {
    position: absolute; left: 0; right: 0; top: 232px; text-align: center;
    font-family: "Lato", sans-serif; font-size: 12px; letter-spacing: 6px;
    color: rgba(255,255,255,0.85);
  }

  .back-shapes { position: absolute; inset: 0; }
  .back-brand {
    position: absolute; left: 62px; top: 118px;
    display: flex; align-items: center; gap: 16px;
  }
  .back-brand .mark { width: 52px; height: 52px; background: var(--blue); }
  .back-brand .divider { width: 2px; height: 64px; background: var(--blue); }
  .back-brand .brand-name {
    font-family: "Cinzel", serif; font-weight: 400; color: var(--blue);
    font-size: 40px; line-height: 1; letter-spacing: 1px;
  }
  .back-brand .brand-sub {
    font-family: "Cinzel", serif; font-weight: 400; color: var(--blue);
    font-size: 14px; letter-spacing: 5px; margin-top: 6px;
  }
  .contact-list {
    position: absolute; left: 30px; top: 250px; list-style: none;
  }
  .contact-list li {
    display: flex; align-items: center; gap: 8px;
    font-size: 12.5px; line-height: 20px; color: var(--text);
  }
  .contact-list .dot { width: 12px; height: 12px; border-radius: 50%; background: var(--blue); flex: none; }
  .attorney-name {
    position: absolute; right: 40px; bottom: 26px;
    font-family: "Cinzel", serif; font-weight: 600; font-size: 17px;
    color: var(--blue); letter-spacing: 1px;
  }
</style>
</head>
<body>

<section class="card card-front" aria-label="Card front">
  <div class="front-brand">
    <span class="mark"></span>
    <span class="brand-name">Harlow Law Offices</span>
  </div>
  <p class="front-web">www.harlowlo.example</p>
</section>

<section class="card card-back" aria-label="Card back">
  <svg class="back-shapes" width="700" height="400" viewBox="0 0 700 400" aria-hidden="true">
    <defs>
      <linearGradient id="blueSweep" x1="0" y1="0" x2="1" y2="1">
        <stop offset="0" stop-color="#2a6ee0"/>
        <stop offset="1" stop-color="#0c3a9c"/>
      </linearGradient>
    </defs>
    <path d="M400 0 L700 0 L700 320 C660 200 560 80 400 0 Z" fill="url(#blueSweep)"/>
    <path d="M0 62 C150 24 300 8 440 12 C320 22 160 48 0 84 Z" fill="#111418"/>
    <path d="M0 90 C140 54 290 34 440 30 C300 46 150 74 0 108 Z" fill="url(#blueSweep)"/>
  </svg>

  <div class="back-brand">
    <span class="mark"></span>
    <span class="divider"></span>
    <div>
      <div class="brand-name">HARLOW</div>
      <div class="brand-sub">LAW OFFICES</div>
    </div>
  </div>

  <ul class="contact-list">
    <li><span class="dot"></span>482 N.E. 3rd Avenue, Suite 2206</li>
    <li><span class="dot"></span>Miami, Florida 33130</li>
    <li><span class="dot"></span>T 305.555.0142</li>
    <li><span class="dot"></span>F 305.555.0143</li>
    <li><span class="dot"></span>dph@harlowlo.example</li>
    <li><span class="dot"></span>www.harlowlo.example</li>
  </ul>

  <p class="attorney-name">Dorian P. Harlow, Esq.</p>
</section>

</body>
</html>
```